TK & LJ Shearing Pty Ltd

We already have an existing logo created by Lumen Guild however we have restructured to a company. We would like someone to add Pty Ltd to our business name please.

Colors

Designer to choose only greyscale colors for use in the design.

```html
<!DOCTYPE html>
<html lang="en">
<head>
<meta charset="utf-8">
<title>TK &amp; LJ Shearing Pty Ltd — Business Cards</title>
<link href="https://fonts.googleapis.com/css2?family=Lora:wght@400;700&display=swap" rel="stylesheet">
<style>
  :root {
    --ink: #111111;
    --paper: #ffffff;
    --backdrop: #e4e7e7;
    --edge: #cfd2d2;
  }
  * { box-sizing: border-box; margin: 0; padding: 0; }
  html, body {
    width: 1200px; height: 900px; overflow: hidden;
    background: var(--backdrop);
    font-family: "Lora", Georgia, serif;
  }
  .sheet {
    width: 1200px; height: 900px;
    display: flex; flex-direction: column;
    align-items: center; justify-content: center; gap: 40px;
  }
  .card {
    position: relative;
    width: 700px; height: 400px;
    padding: 70px 64px 0 64px;
    border: 1px solid var(--edge);
  }
  .card--light { background: var(--paper); color: var(--ink); --icon-bg: var(--ink); --icon-fg: var(--paper); }
  .card--dark  { background: var(--ink); color: var(--paper); --icon-bg: var(--paper); --icon-fg: var(--ink); border-color: var(--ink); }

  .wordmark {
    display: flex; align-items: center; gap: 18px;
  }
  .wordmark__dot {
    width: 64px; height: 64px; border-radius: 50%;
    background: currentColor; flex: none;
  }
  .wordmark__name {
    font-weight: 700; font-size: 44px; line-height: 1.05; letter-spacing: 0.5px;
  }
  .wordmark__suffix { font-size: 44px; }

  .contact {
    list-style: none;
    margin-top: 62px;
    display: flex; flex-direction: column; gap: 12px;
  }
  .contact__item {
    display: flex; align-items: center; gap: 16px;
    font-size: 21px; font-weight: 400;
  }
  .contact__icon {
    width: 34px; height: 34px; flex: none;
  }
  .contact__icon circle { fill: var(--icon-bg); }
  .contact__icon .glyph { fill: var(--icon-fg); }
  .contact__icon .stroke { fill: none; stroke: var(--icon-bg); stroke-width: 1.6; }
</style>
</head>
<body>
<main class="sheet">

  <section class="card card--light" aria-label="Business card, light version">
    <div class="wordmark">
      <span class="wordmark__dot" aria-hidden="true"></span>
      <span class="wordmark__name">TK &amp; LJ Shearing <span class="wordmark__suffix">Pty Ltd</span></span>
    </div>
    <ul class="contact">
      <li class="contact__item">
        <svg class="contact__icon" viewBox="0 0 34 34" aria-hidden="true"><circle cx="17" cy="17" r="17"/><path class="glyph" d="M17 7a6.5 6.5 0 0 0-6.5 6.5C10.5 18.5 17 26 17 26s6.5-7.5 6.5-12.5A6.5 6.5 0 0 0 17 7zm0 9a2.5 2.5 0 1 1 0-5 2.5 2.5 0 0 1 0 5z"/></svg>
        PO Box 418 Brookvale Downs, WA 6599
      </li>
      <li class="contact__item">
        <svg class="contact__icon" viewBox="0 0 34 34" aria-hidden="true"><circle cx="17" cy="17" r="17"/><path class="glyph" d="M12.5 8.5l3 3.5-1.8 2.2c.9 2 2.4 3.6 4.4 4.6l2.1-1.8 3.5 3-1.5 3.2c-6.5-.6-11.6-5.8-12.2-12.2z"/></svg>
        Col +61 412 555 019
      </li>
      <li class="contact__item">
        <svg class="contact__icon" viewBox="0 0 34 34" aria-hidden="true"><circle cx="17" cy="17" r="17"/><rect class="glyph" x="8" y="11" width="18" height="12" rx="1"/><path class="stroke" d="M8.5 11.5L17 18l8.5-6.5"/></svg>
        tkljshearing@example.com
      </li>
    </ul>
  </section>

  <section class="card card--dark" aria-label="Business card, dark version">
    <div class="wordmark">
      <span class="wordmark__dot" aria-hidden="true"></span>
      <span class="wordmark__name">TK &amp; LJ Shearing <span class="wordmark__suffix">Pty Ltd</span></span>
    </div>
    <ul class="contact">
      <li class="contact__item">
        <svg class="contact__icon" viewBox="0 0 34 34" aria-hidden="true"><circle cx="17" cy="17" r="17"/><path class="glyph" d="M17 7a6.5 6.5 0 0 0-6.5 6.5C10.5 18.5 17 26 17 26s6.5-7.5 6.5-12.5A6.5 6.5 0 0 0 17 7zm0 9a2.5 2.5 0 1 1 0-5 2.5 2.5 0 0 1 0 5z"/></svg>
        PO Box 418 Brookvale Downs, WA 6599
      </li>
      <li class="contact__item">
        <svg class="contact__icon" viewBox="0 0 34 34" aria-hidden="true"><circle cx="17" cy="17" r="17"/><path class="glyph" d="M12.5 8.5l3 3.5-1.8 2.2c.9 2 2.4 3.6 4.4 4.6l2.1-1.8 3.5 3-1.5 3.2c-6.5-.6-11.6-5.8-12.2-12.2z"/></svg>
        Col +61 412 555 019
      </li>
      <li class="contact__item">
        <svg class="contact__icon" viewBox="0 0 34 34" aria-hidden="true"><circle cx="17" cy="17" r="17"/><rect class="glyph" x="8" y="11" width="18" height="12" rx="1"/><path class="stroke" d="M8.5 11.5L17 18l8.5-6.5"/></svg>
        tkljshearing@example.com
      </li>
    </ul>
  </section>

</main>
</body>
</html>
```